Willowmere Wellness Academy (Massage School) Flyer Advertisment

We are a massage therapy/holistic healing school, operating in Los Angeles for over 16 years. We need a flyer/advertisement with the aim of attracting new students and potential future massage therapists. Our vision is a 4x6 (read vertical) flyer (potentially dual sided, due to amount of copy we have). The key aesthetic terms for this project are modern, feminine, minimal, natural, fun. The design should be eye catching yet feel organic (we want an advertisement, but keep in mind we are a holistic health institution.) We would like the primary color scheme to be focused around purple and white (green or beige are secondary), and would very much like to see the use of a literal Lavender plant (or multiple) included creatively. You do not need to use all the files we provided. Mandatory is the inclusion of ALL the copy provided in the word document attached, arranged at your discretion, as well as the logo file. We have also provided a picture of our school as well as a few massage photos to possibly be used (only if applicable). Please feel free to be creative with the exact font choices and exact color choices (we only selected the options here as reference.) Thank you all so much for your time and we look forward to reviewing the designs. *Note* we have selected a 5 day duration due to urgency but may be willing to extend for the right designer (please reach out to us if need be)

Target Market(s)

Potential students to become massage therapists or holistic health professionals

Industry/Entity Type

Education

Font styles to use
Sans Serif
Script

Colors
6b449b
ffffff
fbc994
9bcb3c

Requirements
Must have
• Use of Copy attached. Use of logo. use of Lavender plant
Nice to have
• Photo our school (included). Photos of massages being done on clients (examples included)
• * Would be great if you could allow room for rounded corners on the print job* not necessary

```html
<!DOCTYPE html>
<html lang="en">
<head>
<meta charset="utf-8">
<title>Willowmere Wellness Academy Flyer</title>
<link href="https://fonts.googleapis.com/css2?family=Open+Sans:wght@300;400;600;700&display=swap" rel="stylesheet">
<style>
:root{
  --purple:#6b449b;
  --purple-deep:#55307f;
  --purple-text:#6a3f9a;
  --peach:#fbc994;
  --peach-soft:#fde3c6;
  --white:#ffffff;
  --paper:#f5f4f6;
  --ink:#4a4a4a;
  --stage:#e9e8ea;
}
*{margin:0;padding:0;box-sizing:border-box}
html,body{width:1200px;height:885px;overflow:hidden;background:var(--stage);font-family:"Open Sans",sans-serif;color:var(--ink)}
.flyer{position:absolute;top:76px;width:488px;height:734px;background:linear-gradient(#fff 0%,#fff 45%,var(--paper) 100%);overflow:hidden;box-shadow:0 4px 14px rgba(0,0,0,.18)}
.flyer--front{left:92px}
.flyer--back{left:632px}
.photo{position:absolute;left:0;top:0;width:100%}
.front-photo{height:340px;background:linear-gradient(120deg,#f4ece6 0%,#e9c2a8 45%,#f2e3da 75%,#e6f0d8 100%)}
.back-photo{height:250px;background:linear-gradient(100deg,#7a5a44 0%,#6b5548 25%,#b9a3c9 55%,#a98fc0 80%,#cbb6de 100%)}
.swoop{position:absolute;left:0;width:488px}
.building{position:absolute;left:332px;top:185px;width:192px;height:192px;border-radius:50%;border:6px solid #fff;background:linear-gradient(160deg,#bcd3ea 0%,#cfd5da 45%,#5e5b56 75%,#6c7a4e 100%);box-shadow:0 2px 6px rgba(0,0,0,.2)}
.badge{position:absolute;border-radius:50%;background:#fff;border:4px solid var(--purple);display:flex;align-items:center;justify-content:center;text-align:center;color:var(--purple);font-weight:600;line-height:1.2;box-shadow:0 2px 6px rgba(0,0,0,.2)}
.flyer--front .badge{left:282px;top:250px;width:104px;height:104px;font-size:11px;padding:10px}
.flyer--back .badge{left:361px;top:156px;width:110px;height:110px;font-size:11.5px;padding:10px}
.headline{position:absolute;top:366px;width:100%;text-align:center;color:var(--purple-text);font-weight:400;font-size:31px;line-height:42px}
.courses{position:absolute;top:464px;left:20px;right:20px;text-align:center;font-size:14.5px;line-height:20.5px;color:#555}
.pill{position:absolute;background:var(--peach);border:2px solid var(--peach-soft);border-radius:18px;color:var(--purple-text);font-weight:700;text-align:center;white-space:nowrap;box-shadow:0 8px 8px -6px rgba(0,0,0,.25)}
.pill--open-house{left:77px;top:579px;width:339px;height:32px;line-height:28px;font-size:15px;letter-spacing:.6px}
.pill--reviews{left:119px;top:556px;width:250px;height:24px;font-size:9.5px;letter-spacing:.2px;display:flex;align-items:center;justify-content:center;gap:6px}
.pill--reviews .dot{width:9px;height:9px;border-radius:50%;background:var(--purple);flex:none}
.footer{position:absolute;left:0;bottom:0;width:488px;height:92px}
.footer svg{position:absolute;left:0;top:0}
.footer-text{position:absolute;left:0;right:0;top:30px;text-align:center;color:#fff;font-size:12.5px;line-height:17px}
.footer-text .web{font-size:15px;font-weight:700;letter-spacing:.8px;margin-top:4px}
.intro{position:absolute;left:28px;top:256px;color:var(--purple-text);font-size:14px;line-height:19px}
.benefits{position:absolute;left:28px;top:301px;right:18px;list-style:none;font-size:13.5px;line-height:23px;color:#4f4f4f}
.benefits li{position:relative;padding-left:20px}
.benefits li::before{content:"";position:absolute;left:0;top:7px;width:10px;height:10px;border-radius:50%;background:var(--peach)}
.thumb{position:absolute;top:436px;width:98px;height:98px;border-radius:50%;border:5px solid #fff;box-shadow:0 3px 8px rgba(0,0,0,.2)}
.thumb--one{left:68px;background:radial-gradient(circle at 45% 45%,#d9ab96,#a87565)}
.thumb--two{left:195px;background:radial-gradient(circle at 50% 45%,#f0a040,#b4521a)}
.thumb--three{left:321px;background:radial-gradient(circle at 50% 45%,#fbc7a8,#ee9a72)}
.licensing{position:absolute;left:40px;right:40px;top:596px;text-align:center;font-size:10px;line-height:12.2px;color:#555}
</style>
</head>
<body>

<section class="flyer flyer--front">
  <div class="photo front-photo" role="img" aria-label="Photo of a woman receiving a relaxing back massage"></div>
  <svg class="swoop" style="top:220px" width="488" height="160" viewBox="0 0 488 160">
    <path d="M0 170 L0 120 Q120 70 488 60 L488 170Z" fill="#fff"/>
    <path d="M0 120 Q110 72 360 66 Q180 60 0 100Z" fill="var(--purple)"/>
    <path d="M50 145 Q120 112 280 112" fill="none" stroke="var(--peach)" stroke-width="6" stroke-linecap="round"/>
  </svg>
  <div class="building" role="img" aria-label="Photo of the academy building"></div>
  <div class="badge">Willowmere Wellness Academy</div>
  <h1 class="headline">Become a Certified<br>MASSAGE THERAPIST!</h1>
  <p class="courses">WWA offers courses in Swedish, Deep Tissue, Myofascial Release, Chair Massage, Aromatherapy, Energy Healing, Crystal &amp; Gemstone Therapy, Shiatsu, Lymphatic, Sports Massage, Pregnan-cy Massage, Hot Stone Massage, Polarity Therapy and more!</p>
  <div class="pill pill--open-house">ASK US ABOUT OUR NEXT OPEN HOUSE</div>
  <footer class="footer">
    <svg width="488" height="92" viewBox="0 0 488 92">
      <defs><linearGradient id="bandFront" x1="0" x2="1"><stop offset="0" stop-color="var(--purple)"/><stop offset="1" stop-color="var(--purple-deep)"/></linearGradient></defs>
      <path d="M0 20 Q244 -12 488 20" fill="none" stroke="var(--purple)" stroke-width="1.5"/>
      <path d="M0 28 Q244 -6 488 28 L488 92 L0 92Z" fill="url(#bandFront)"/>
    </svg>
    <div class="footer-text">
      <div>Willowmere Wellness Academy</div>
      <div>2140 Larkspur Ave., Los Angeles, CA 91046 | (818) 555-0147</div>
      <div class="web">www.willowmereacademy.org</div>
    </div>
  </footer>
</section>

<section class="flyer flyer--back">
  <div class="photo back-photo" role="img" aria-label="Photo of an essential oil bottle, lavender soap and bath salts"></div>
  <svg class="swoop" style="top:190px" width="488" height="80" viewBox="0 0 488 80">
    <path d="M0 80 L0 52 Q150 20 488 40 L488 80Z" fill="#fff"/>
    <path d="M0 58 Q150 12 488 24 L488 36 Q200 26 0 64Z" fill="var(--purple)"/>
  </svg>
  <div class="badge">Willowmere Wellness Academy</div>
  <p class="intro">WWA has been educating students from<br>around the world and all walks of life for over 16 years!</p>
  <ul class="benefits">
    <li>Complete an affordable 300 CEU Hour Program in 15 Weeks</li>
    <li>2500+ Hours of Advanced Electives in various modalities</li>
    <li>Many classes open to the public and non-body-workers</li>
    <li>Study with accomplished holistic healers and seasoned health professionals</li>
  </ul>
  <div class="thumb thumb--one" role="img" aria-label="Photo of hands massaging a back"></div>
  <div class="thumb thumb--two" role="img" aria-label="Photo of an oil massage in warm light"></div>
  <div class="thumb thumb--three" role="img" aria-label="Photo of hands on a shoulder"></div>
  <div class="pill pill--reviews">CHECK OUT OUR REVIEWS ON REVIEWLY! <span class="dot"></span></div>
  <p class="licensing">WWA is licensed to operate by the Office of Vocational School Standards and fully approved by the Western Bodywork Practice Council as well as the Regional Board of Care Professions.</p>
  <footer class="footer">
    <svg width="488" height="92" viewBox="0 0 488 92">
      <defs><linearGradient id="bandBack" x1="0" x2="1"><stop offset="0" stop-color="var(--purple)"/><stop offset="1" stop-color="var(--purple-deep)"/></linearGradient></defs>
      <path d="M0 20 Q244 -12 488 20" fill="none" stroke="var(--purple)" stroke-width="1.5"/>
      <path d="M0 28 Q244 -6 488 28 L488 92 L0 92Z" fill="url(#bandBack)"/>
    </svg>
    <div class="footer-text">
      <div>Willowmere Wellness Academy</div>
      <div>2140 Larkspur Ave., Los Angeles, CA 91046 | (818) 555-0147</div>
      <div class="web">www.willowmereacademy.org</div>
    </div>
  </footer>
</section>

</body>
</html>
```